new service company in the field of construction seeks to make the Creation of a PPT

We need a PPT format with a cover page a frame for presentation. our company is based in Paris which was named VORENTEX. we just did our logo attached. Our company offers services to manage and control documents that pass on projects in construction (building, infrastructure, energy, oil and gas etc. ..). We use internet systems to help us, design must show insurance, quality, and safety. Customers should build any type of works and can not build without the approved documents. These documents go through multiple validations, and vorentex staff seconded on projects, coordinate these processes and documents, quality documents, to ensure that project deadlines are met and project management sees his project developed within the period, through regular reporting. the services offered by our company help ensure the project of building on time, to ensure the project manager visibility on what e will not, and can act accordingly.

Target Market(s)

general contractor of engineering construction or big business masters lumber wholesale real estate investor, project ownership in the construction sector

Industry/Entity Type

Construction

Contact Information for Business Card

carte rectangulaire petite taille (4X6cm env)
horizontale ou verticale
prendre en compte les éléments suivants :
logo
nom de société
adresse postale (4 lignes)
teléphone:
mail
role (ex : directeur)
in the back : La qualité documentaire de vos projets

Font styles to use
Sans Serif

Colors
34a7d7
85cae6
cee9f5
0592cd

Requirements
Must have
• The project should have 2 sliders: slider 1. Cover Page 2. slider for the content of presentations THE GOAL IS TO HAVE A VISUAL IDENTITY ON PPT, MY BUSINESS CARDS AND LETTERS must stay in mind and colors of the logo that joined the design must be clean and recall the seriousness, ease. the design must take into account the page numbers Tag line: the documentary quality of your projects information such as tagline and writes must be modifiable
Nice to have
• would require the presentation of the figure shows concepts or reporting table THE GOAL IS TO HAVE A VISUAL IDENTITY ON PPT, MY BUSINESS CARDS AND LETTERS
Should not have
• not to building or building in the logo

```html
<!DOCTYPE html>
<html lang="fr">
<head>
<meta charset="utf-8">
<title>VORENTEX — Modèle de présentation</title>
<link href="https://fonts.googleapis.com/css2?family=Montserrat:wght@500;600;700;800&display=swap" rel="stylesheet">
<style>
  :root{
    --stage:#c9d3d8;
    --panel:#f3f3f3;
    --brand-blue:#2a64ad;
    --brand-light:#6b9bd3;
    --ink:#2b2f36;
    --muted:#7a7d82;
    --callout-fill:#f6dcc8;
    --callout-line:#d5322b;
    --thumb-border:#c6c9cd;
    --text-grey:#9aa0a6;
    --bar-red:#c0392b;
    --bar-brown:#9a6a22;
    --bar-yellow:#e8e81e;
    --olive:#6b6b10;
    --dark-brown:#5a3510;
    --faint:#e3e7eb;
  }
  *{box-sizing:border-box;margin:0;padding:0}
  html,body{width:1200px;height:1200px;overflow:hidden}
  body{background:var(--stage);font-family:'Montserrat',sans-serif;position:relative}

  .sorter{position:absolute;left:36px;top:64px;width:1128px;height:660px;background:var(--panel)}

  .slide{position:absolute;width:192px;height:112px;background:#fff;border:1px solid var(--thumb-border);overflow:hidden}
  .slide.is-selected{outline:3px solid var(--callout-line);outline-offset:1px}
  .slide-number{position:absolute;font:600 16px 'Montserrat',sans-serif;color:var(--muted)}

  /* cover pieces */
  .cover-band{position:absolute;left:2px;right:2px;bottom:2px;height:38px;background:var(--brand-blue)}
  .cover-band .band-title{position:absolute;left:12px;top:11px;font:700 5.4px 'Montserrat',sans-serif;color:#fff;letter-spacing:.1px}
  .cover-band .band-rule{position:absolute;left:12px;top:21px;width:92px;height:1px;background:#fff}
  .cover-photo{position:absolute;left:2px;right:2px;top:2px;bottom:40px;background:linear-gradient(120deg,#b7c1c8 0%,#e9ecee 38%,#aab4bb 70%,#cfd6da 100%)}
  .brand-name{position:absolute;font:800 8px 'Montserrat',sans-serif;color:var(--brand-blue);letter-spacing:.2px}
  .brand-dot{position:absolute;border-radius:50%;background:var(--brand-blue)}

  .callout{position:absolute;background:var(--callout-fill);border:1px solid var(--callout-line);font:600 3.4px 'Montserrat',sans-serif;color:var(--callout-line);padding:3px}
  .callout.small{height:10px;padding:2px 3px}

  /* content pieces */
  .top-rule{position:absolute;left:2px;right:2px;top:2px;height:2px;background:var(--brand-blue)}
  .bottom-rule{position:absolute;left:2px;right:2px;bottom:3px;height:2px;background:var(--brand-blue)}
  .slide-title{position:absolute;left:14px;top:9px;font:600 5px 'Montserrat',sans-serif;color:var(--ink)}
  .slide-sub{position:absolute;left:14px;top:16px;font:600 3px 'Montserrat',sans-serif;color:var(--brand-blue)}
  .corner-brand{position:absolute;right:6px;top:6px;width:40px;height:16px}
  .corner-brand .brand-dot{width:8px;height:8px;right:8px;top:0}
  .corner-brand .brand-name{right:0;top:9px;font-size:4px}
  .photo{position:absolute;top:30px;width:82px;height:52px}
  .photo.gears{background:linear-gradient(135deg,#3b3426,#8c7a55 45%,#2c2a26)}
  .photo.lab{background:linear-gradient(135deg,#1f2b33,#6f8a94 50%,#1c2328)}
  .text-col{position:absolute;top:86px;width:82px}
  .text-col i{display:block;height:1.2px;background:var(--text-grey);margin-bottom:2.4px}

  .section-head{position:absolute;left:14px;top:38px;font:600 3.6px 'Montserrat',sans-serif;color:var(--ink)}
  .bullets{position:absolute;left:16px;top:48px;width:80px}
  .bullets i{display:block;height:1.1px;background:var(--text-grey);margin-bottom:2.2px}
  .bullets i.gap{margin-bottom:6px}

  .tile{position:absolute;width:26px;height:10px;font:600 3px 'Montserrat',sans-serif;color:#fff;display:flex;align-items:center;justify-content:center}

  .chart{position:absolute;left:112px;top:34px}
  .footer-band{position:absolute;left:2px;right:2px;bottom:2px;height:5px}

  .faint-circle{position:absolute;border-radius:50%;background:var(--faint)}
  .para{position:absolute;font:500 3.5px/5.6px 'Montserrat',sans-serif;color:var(--ink);overflow:hidden}
  .para-title{position:absolute;font:700 7px 'Montserrat',sans-serif;color:var(--brand-blue)}

  .closing{background:linear-gradient(90deg,#4a86cf,#2a64ad 60%,#1f55a0)}
  .closing-disc{position:absolute;left:30px;top:-18px;width:148px;height:148px;border-radius:50%;background:#fff}
  .contact-panel{position:absolute;left:2px;top:2px;bottom:2px;width:72px;background:var(--brand-blue);color:#fff}
  .contact-panel .head{position:absolute;left:14px;top:30px;font:600 4px 'Montserrat',sans-serif}
  .contact-panel .line{position:absolute;left:0;right:0;text-align:center;font:500 2.8px 'Montserrat',sans-serif}
</style>
</head>
<body>
<main class="sorter" aria-label="Modèle de présentation VORENTEX">

  <!-- Row 1 : covers -->
  <section class="slide is-selected" style="left:10px;top:8px">
    <div class="cover-band"><span class="band-title">LOREM IPSUM DOLOR SIT AMET</span><span class="band-rule"></span></div>
    <div class="callout" style="left:8px;top:12px;width:40px;height:28px">Légende image</div>
    <span class="brand-dot" style="left:108px;top:6px;width:72px;height:72px"></span>
    <span class="brand-name" style="left:54px;top:62px">VORENTEX</span>
  </section>
  <span class="slide-number" style="left:13px;top:124px">1</span>

  <section class="slide" style="left:234px;top:8px">
    <div class="cover-photo" role="img" aria-label="Photo de deux alpinistes s'entraidant sur un sommet au lever du soleil"></div>
    <div class="cover-band"><span class="band-title">LOREM IPSUM DOLOR SIT AMET</span><span class="band-rule"></span></div>
    <div class="callout" style="left:8px;top:12px;width:40px;height:28px">Légende image</div>
    <span class="brand-dot" style="left:108px;top:6px;width:72px;height:72px"></span>
    <span class="brand-name" style="left:54px;top:62px">VORENTEX</span>
  </section>
  <span class="slide-number" style="left:237px;top:124px">2</span>

  <section class="slide" style="left:458px;top:8px">
    <div class="cover-band"><span class="band-title">LOREM IPSUM DOLOR SIT AMET</span><span class="band-rule"></span></div>
    <div class="callout small" style="left:6px;top:8px;width:36px">Titre</div>
    <span class="brand-dot" style="left:126px;top:28px;width:50px;height:50px"></span>
    <span class="brand-name" style="left:66px;top:58px">VORENTEX</span>
  </section>
  <span class="slide-number" style="left:461px;top:124px">3</span>

  <section class="slide" style="left:682px;top:8px">
    <div class="cover-photo" role="img" aria-label="Photo de deux alpinistes s'entraidant sur un sommet au lever du soleil"></div>
    <div class="cover-band"><span class="band-title">LOREM IPSUM DOLOR SIT AMET</span><span class="band-rule"></span></div>
    <div class="callout small" style="left:6px;top:8px;width:36px">Titre</div>
    <span class="brand-dot" style="left:126px;top:28px;width:50px;height:50px"></span>
    <span class="brand-name" style="left:66px;top:58px">VORENTEX</span>
  </section>
  <span class="slide-number" style="left:685px;top:124px">4</span>

  <section class="slide" style="left:905px;top:8px">
    <div class="cover-band"><span class="band-title">LOREM IPSUM DOLOR SIT AMET</span><span class="band-rule"></span></div>
    <div class="callout small" style="left:6px;top:8px;width:36px">Titre</div>
    <span class="brand-name" style="left:120px;top:18px">VORENTEX</span>
    <span class="brand-dot" style="left:120px;top:32px;width:40px;height:40px"></span>
  </section>
  <span class="slide-number" style="left:908px;top:124px">5</span>

  <!-- Row 2 -->
  <section class="slide" style="left:10px;top:172px">
    <div class="cover-photo" role="img" aria-label="Photo de deux alpinistes s'entraidant sur un sommet au lever du soleil"></div>
    <div class="cover-band"><span class="band-title">LOREM IPSUM DOLOR SIT AMET</span><span class="band-rule"></span></div>
    <div class="callout small" style="left:6px;top:8px;width:36px">Titre</div>
    <span class="brand-name" style="left:120px;top:18px">VORENTEX</span>
    <span class="brand-dot" style="left:120px;top:32px;width:40px;height:40px"></span>
  </section>
  <span class="slide-number" style="left:13px;top:288px">6</span>

  <section class="slide" style="left:234px;top:172px">
    <div class="cover-band"><span class="band-title">LOREM IPSUM DOLOR SIT AMET</span><span class="band-rule"></span></div>
    <div class="callout small" style="left:6px;top:8px;width:36px">Titre</div>
    <span class="brand-name" style="left:86px;top:54px">VORENTEX</span>
    <span class="brand-dot" style="left:138px;top:44px;width:32px;height:32px"></span>
  </section>
  <span class="slide-number" style="left:237px;top:288px">7</span>

  <section class="slide" style="left:458px;top:172px">
    <div class="cover-photo" role="img" aria-label="Photo de deux alpinistes s'entraidant sur un sommet au lever du soleil"></div>
    <div class="cover-band"><span class="band-title">LOREM IPSUM DOLOR SIT AMET</span><span class="band-rule"></span></div>
    <div class="callout small" style="left:6px;top:8px;width:36px">Titre</div>
    <span class="brand-name" style="left:86px;top:54px">VORENTEX</span>
    <span class="brand-dot" style="left:138px;top:44px;width:32px;height:32px"></span>
  </section>
  <span class="slide-number" style="left:461px;top:288px">8</span>

  <section class="slide" style="left:682px;top:172px">
    <span class="top-rule"></span>
    <span class="slide-title">LOREM IPSUM DOLOR SIT AMET</span>
    <span class="slide-sub">Lorem ipsum dolor sit amet</span>
    <div class="corner-brand"><span class="brand-dot"></span><span class="brand-name">VORENTEX</span></div>
    <div class="photo gears" style="left:12px" role="img" aria-label="Photo d'engrenages mécaniques industriels"></div>
    <div class="photo lab" style="left:98px" role="img" aria-label="Photo d'un équipement technique éclairé"></div>
    <div class="callout small" style="left:8px;top:26px;width:28px">Légende</div>
    <div class="text-col" style="left:12px"><i></i><i></i><i></i><i style="width:70%"></i></div>
    <div class="text-col" style="left:98px"><i></i><i></i><i></i><i style="width:60%"></i></div>
    <span class="bottom-rule"></span>
  </section>
  <span class="slide-number" style="left:685px;top:288px">9</span>

  <section class="slide" style="left:905px;top:172px">
    <span class="top-rule"></span>
    <span class="slide-title">LOREM IPSUM DOLOR SIT AMET</span>
    <span class="slide-sub">Lorem ipsum dolor sit amet</span>
    <div class="corner-brand"><span class="brand-dot"></span><span class="brand-name">VORENTEX</span></div>
    <div class="photo gears" style="left:12px" role="img" aria-label="Photo d'engrenages mécaniques industriels"></div>
    <div class="photo lab" style="left:98px" role="img" aria-label="Photo d'un équipement technique éclairé"></div>
    <div class="callout small" style="left:8px;top:26px;width:28px">Légende</div>
    <div class="text-col" style="left:12px"><i></i><i></i><i></i><i style="width:70%"></i></div>
    <div class="text-col" style="left:98px"><i></i><i></i><i></i><i style="width:60%"></i></div>
    <span class="bottom-rule"></span>
  </section>
  <span class="slide-number" style="left:908px;top:288px">10</span>

  <!-- Row 3 -->
  <section class="slide" style="left:10px;top:336px">
    <span class="top-rule"></span>
    <span class="slide-title">LOREM IPSUM DOLOR SIT AMET</span>
    <span class="slide-sub">Lorem ipsum dolor sit amet</span>
    <div class="corner-brand"><span class="brand-dot"></span><span class="brand-name">VORENTEX</span></div>
    <span class="section-head">Lorem ipsum</span>
    <div class="bullets"><i></i><i></i><i class="gap"></i><i></i><i class="gap"></i><i></i><i></i><i></i></div>
    <div class="callout" style="left:52px;top:27px;width:54px;height:12px;text-align:center">Zone de commentaire</div>
    <span class="tile" style="left:112px;top:42px;background:var(--brand-blue)">Étude</span>
    <span class="tile" style="left:146px;top:42px;background:var(--olive)">Suivi</span>
    <span class="tile" style="left:112px;top:56px;background:var(--bar-red)">Visa</span>
    <span class="tile" style="left:146px;top:56px;background:var(--bar-yellow);color:var(--ink)">Plans</span>
    <span class="tile" style="left:112px;top:70px;background:var(--bar-brown)">Audit</span>
    <span class="tile" style="left:146px;top:70px;background:var(--dark-brown)">Rapport</span>
    <span class="bottom-rule"></span>
  </section>
  <span class="slide-number" style="left:13px;top:452px">11</span>

  <section class="slide" style="left:234px;top:336px">
    <span class="top-rule"></span>
    <span class="slide-title">LOREM IPSUM DOLOR SIT AMET</span>
    <span class="slide-sub">Lorem ipsum dolor sit amet</span>
    <div class="corner-brand"><span class="brand-dot"></span><span class="brand-name">VORENTEX</span></div>
    <span class="section-head">Lorem ipsum</span>
    <div class="bullets"><i></i><i></i><i class="gap"></i><i></i><i class="gap"></i><i></i><i></i><i></i></div>
    <div class="callout small" style="left:38px;top:28px;width:46px;text-align:center">Commentaire</div>
    <svg class="chart" width="70" height="68" viewBox="0 0 70 68" aria-label="Histogramme">
      <g><rect x="4" y="10" width="2.5" height="40" fill="#2a64ad"/><rect x="7" y="22" width="2.5" height="28" fill="#9a6a22"/><rect x="10" y="28" width="2.5" height="22" fill="#c0392b"/></g>
      <g><rect x="26" y="20" width="2.5" height="30" fill="#2a64ad"/><rect x="29" y="8" width="2.5" height="42" fill="#9a6a22"/><rect x="32" y="30" width="2.5" height="20" fill="#c0392b"/></g>
      <g><rect x="48" y="16" width="2.5" height="34" fill="#2a64ad"/><rect x="51" y="34" width="2.5" height="16" fill="#9a6a22"/><rect x="54" y="24" width="2.5" height="26" fill="#c0392b"/></g>
      <g font-family="Montserrat, sans-serif" font-size="3" fill="#2b2f36"><text x="6" y="56">Lot</text><text x="28" y="56">Lot</text><text x="50" y="56">Lot</text></g>
      <g><rect x="16" y="62" width="4" height="1.5" fill="#2a64ad"/><rect x="30" y="62" width="4" height="1.5" fill="#9a6a22"/><rect x="44" y="62" width="4" height="1.5" fill="#c0392b"/></g>
    </svg>
    <span class="footer-band" style="background:var(--bar-brown)"></span>
  </section>
  <span class="slide-number" style="left:237px;top:452px">12</span>

  <section class="slide" style="left:458px;top:336px">
    <span class="top-rule"></span>
    <span class="slide-title">LOREM IPSUM DOLOR SIT AMET</span>
    <span class="slide-sub">Lorem ipsum dolor sit amet</span>
    <div class="corner-brand"><span class="brand-dot"></span><span class="brand-name">VORENTEX</span></div>
    <span class="section-head">Lorem ipsum</span>
    <div class="bullets"><i></i><i></i><i class="gap"></i><i></i><i class="gap"></i><i></i><i></i><i></i></div>
    <div class="callout small" style="left:38px;top:28px;width:46px;text-align:center">Commentaire</div>
    <svg class="chart" width="70" height="68" viewBox="0 0 70 68" aria-label="Histogramme">
      <g><rect x="4" y="10" width="2.5" height="40" fill="#2a64ad"/><rect x="7" y="22" width="2.5" height="28" fill="#e8e81e"/><rect x="10" y="28" width="2.5" height="22" fill="#c0392b"/></g>
      <g><rect x="26" y="20" width="2.5" height="30" fill="#2a64ad"/><rect x="29" y="8" width="2.5" height="42" fill="#e8e81e"/><rect x="32" y="30" width="2.5" height="20" fill="#c0392b"/></g>
      <g><rect x="48" y="16" width="2.5" height="34" fill="#2a64ad"/><rect x="51" y="34" width="2.5" height="16" fill="#e8e81e"/><rect x="54" y="24" width="2.5" height="26" fill="#c0392b"/></g>
      <g font-family="Montserrat, sans-serif" font-size="3" fill="#2b2f36"><text x="6" y="56">Lot</text><text x="28" y="56">Lot</text><text x="50" y="56">Lot</text></g>
      <g><rect x="16" y="62" width="4" height="1.5" fill="#2a64ad"/><rect x="30" y="62" width="4" height="1.5" fill="#e8e81e"/><rect x="44" y="62" width="4" height="1.5" fill="#c0392b"/></g>
    </svg>
    <span class="footer-band" style="background:var(--bar-yellow)"></span>
  </section>
  <span class="slide-number" style="left:461px;top:452px">13</span>

  <section class="slide" style="left:682px;top:336px">
    <span class="top-rule"></span>
    <span class="slide-title">LOREM IPSUM DOLOR SIT AMET</span>
    <span class="slide-sub">Lorem ipsum dolor sit amet</span>
    <div class="corner-brand"><span class="brand-dot"></span><span class="brand-name">VORENTEX</span></div>
    <span class="section-head">Lorem ipsum</span>
    <div class="bullets"><i></i><i></i><i class="gap"></i><i></i><i class="gap"></i><i></i><i></i><i></i></div>
    <div class="callout small" style="left:38px;top:28px;width:46px;text-align:center">Commentaire</div>
    <svg class="chart" width="70" height="68" viewBox="0 0 70 68" aria-label="Histogramme">
      <g><rect x="4" y="10" width="2.5" height="40" fill="#2a64ad"/><rect x="7" y="22" width="2.5" height="28" fill="#6b9bd3"/><rect x="10" y="28" width="2.5" height="22" fill="#c0392b"/></g>
      <g><rect x="26" y="20" width="2.5" height="30" fill="#2a64ad"/><rect x="29" y="8" width="2.5" height="42" fill="#6b9bd3"/><rect x="32" y="30" width="2.5" height="20" fill="#c0392b"/></g>
      <g><rect x="48" y="16" width="2.5" height="34" fill="#2a64ad"/><rect x="51" y="34" width="2.5" height="16" fill="#6b9bd3"/><rect x="54" y="24" width="2.5" height="26" fill="#c0392b"/></g>
      <g font-family="Montserrat, sans-serif" font-size="3" fill="#2b2f36"><text x="6" y="56">Lot</text><text x="28" y="56">Lot</text><text x="50" y="56">Lot</text></g>
      <g><rect x="16" y="62" width="4" height="1.5" fill="#2a64ad"/><rect x="30" y="62" width="4" height="1.5" fill="#6b9bd3"/><rect x="44" y="62" width="4" height="1.5" fill="#c0392b"/></g>
    </svg>
    <span class="footer-band" style="background:var(--bar-red)"></span>
  </section>
  <span class="slide-number" style="left:685px;top:452px">14</span>

  <section class="slide" style="left:905px;top:336px">
    <span class="top-rule"></span>
    <span class="faint-circle" style="left:10px;top:2px;width:110px;height:110px"></span>
    <div class="corner-brand"><span class="brand-dot"></span><span class="brand-name">VORENTEX</span></div>
    <span class="para-title" style="left:72px;top:18px">Lorem ipsum</span>
    <p class="para" style="left:26px;top:30px;width:140px;height:58px;text-align:center">Lorem ipsum dolor sit amet consectetur adipiscing elit sed do eiusmod tempor incididunt ut labore et dolore magna aliqua ut enim ad minim veniam quis nostrud exercitation ullamco laboris nisi ut aliquip ex ea commodo consequat duis aute irure dolor in reprehenderit.</p>
    <span class="bottom-rule"></span>
  </section>
  <span class="slide-number" style="left:908px;top:452px">15</span>

  <!-- Row 4 -->
  <section class="slide" style="left:10px;top:500px">
    <span class="top-rule"></span>
    <span class="faint-circle" style="left:104px;top:6px;width:96px;height:96px"></span>
    <div class="corner-brand"><span class="brand-dot"></span><span class="brand-name">VORENTEX</span></div>
    <span class="para-title" style="left:12px;top:14px">Lorem ipsum</span>
    <p class="para" style="left:12px;top:26px;width:84px;height:72px">Lorem ipsum dolor sit amet consectetur adipiscing elit sed do eiusmod tempor incididunt ut labore et dolore magna aliqua ut enim ad minim veniam quis nostrud exercitation ullamco laboris nisi ut aliquip ex ea commodo.</p>
    <span class="bottom-rule"></span>
  </section>
  <span class="slide-number" style="left:13px;top:616px">16</span>

  <section class="slide" style="left:234px;top:500px">
    <span class="top-rule"></span>
    <span class="faint-circle" style="left:-20px;top:18px;width:90px;height:90px"></span>
    <div class="corner-brand"><span class="brand-dot"></span><span class="brand-name">VORENTEX</span></div>
    <span class="para-title" style="left:80px;top:20px">Lorem ipsum</span>
    <p class="para" style="left:40px;top:32px;width:130px;height:58px;text-align:center">Lorem ipsum dolor sit amet consectetur adipiscing elit sed do eiusmod tempor incididunt ut labore et dolore magna aliqua ut enim ad minim veniam quis nostrud exercitation ullamco laboris nisi ut aliquip ex ea commodo consequat.</p>
    <span class="bottom-rule"></span>
  </section>
  <span class="slide-number" style="left:237px;top:616px">17</span>

  <section class="slide closing" style="left:458px;top:500px">
    <span class="closing-disc"></span>
    <span class="brand-dot" style="left:92px;top:22px;width:22px;height:22px"></span>
    <span class="brand-name" style="left:48px;top:52px;font-size:17px">VORENTEX</span>
    <span style="position:absolute;left:72px;top:88px;font:500 4.5px 'Montserrat',sans-serif;color:var(--brand-light)">Lorem ipsum dolor</span>
  </section>
  <span class="slide-number" style="left:461px;top:616px">18</span>

  <section class="slide" style="left:682px;top:500px">
    <div class="contact-panel">
      <span class="head">Lorem ipsum dolor</span>
      <span class="line" style="top:42px">Nom</span>
      <span class="line" style="top:49px">Rôle</span>
      <span class="line" style="top:56px">Adresse</span>
      <span class="line" style="top:63px">Paris</span>
      <span class="line" style="top:70px">Tél 01 00 00 00 00</span>
      <span class="line" style="top:77px">contact@vorentex.fr</span>
    </div>
    <span class="brand-dot" style="left:118px;top:38px;width:18px;height:18px"></span>
    <span class="brand-name" style="left:94px;top:60px;font-size:13px">VORENTEX</span>
  </section>
  <span class="slide-number" style="left:685px;top:616px">19</span>

</main>
</body>
</html>
```